Generic fund comparison

We need a power point template to be used for presentation decks and proposals to clients and prospects. We are an independent Registered Investment Advisor in Pittsburgh Pennsylvania.
Our services include family office, alternative investments, investment management, financial planning and consulting.
We would like to see designs that use the color green and grey as they are part of our logo and brand image. The final design should communicate our guiding principles: 'educate, plan, implement, adapt'

```html
<!DOCTYPE html>
<html lang="en">
<head>
<meta charset="utf-8">
<title>Veranta – Presentation Template</title>
<link href="https://fonts.googleapis.com/css2?family=Montserrat:wght@300;400;500;600;700;800&family=Poppins:wght@600;700;800&display=swap" rel="stylesheet">
<style>
  :root{
    --page:#150d1a;
    --green:#7dbb2e;
    --green-dark:#68a020;
    --ink:#1c1c1c;
    --text:#333;
    --grey:#6b6b6b;
    --bar-grey:#c9c9c9;
    --white:#ffffff;
    --line:#e3e3e3;
  }
  *{box-sizing:border-box;margin:0;padding:0}
  html,body{width:1200px;height:3839px;overflow:hidden}
  body{background:var(--page);font-family:"Montserrat",sans-serif;color:var(--text);position:relative}
  .slide{position:absolute;left:80px;width:1040px;height:585px;overflow:hidden;background:var(--white)}
  .media{position:absolute}

  /* Cover */
  .cover{top:49px}
  .cover .media{inset:0;background:linear-gradient(180deg,#fbfbfc 0%,#eeecef 28%,#b9b6bb 48%,#5b5a60 70%,#2c2d33 100%)}
  .brand{position:absolute;left:161px;top:45px;width:254px;text-align:center}
  .brand-mark{width:75px;height:75px;background:var(--green);margin:0 auto 22px}
  .brand-name{font-weight:400;font-size:50px;letter-spacing:3px;color:#777;line-height:1}
  .cover-tagline{position:absolute;left:463px;top:62px;font-size:29px;font-weight:400;line-height:35px;color:#222}
  .cover-date{position:absolute;left:463px;top:140px;font-size:36px;font-weight:700;color:#111}
  .cover-date span{color:var(--green)}

  /* Text + photo slides */
  .split .copy{position:absolute;left:0;top:0;width:507px;height:100%;padding:68px 54px 0 54px}
  .split .media{left:507px;top:0;right:0;bottom:0}
  .slide-title{font-weight:400;font-size:34px;color:#222;margin-bottom:20px}
  .slide-sub{font-weight:700;font-size:20px;line-height:32px;letter-spacing:1.5px;text-transform:uppercase;color:#1a1a1a;margin-bottom:20px;padding-left:3px}
  .lead{font-size:12px;line-height:17.5px;color:#333;margin-bottom:20px;padding-left:3px}
  .ticks{list-style:none;padding-left:3px}
  .ticks li{position:relative;padding-left:30px;font-size:12px;line-height:17px;margin-bottom:15px;color:#333}
  .ticks li svg{position:absolute;left:0;top:5px;width:17px;height:17px}
  .intro{top:678px}
  .intro .media{background:linear-gradient(160deg,#d9d9d9 0%,#c4c4c4 45%,#6f8f4c 62%,#b8b8b8 80%,#8e8e8e 100%)}
  .meeting{top:1936px}
  .meeting .media{background:linear-gradient(150deg,#3c3a3d 0%,#8a7a6a 30%,#e7e2db 55%,#b89a7a 78%,#3a3535 100%)}

  /* Services */
  .services{top:1307px}
  .services .media{left:0;top:0;width:523px;bottom:0;background:linear-gradient(160deg,#2e2e2e 0%,#3a3a3a 50%,#262626 100%)}
  .hex-grid{position:absolute;left:0;top:0}
  .services-title{position:absolute;left:817px;top:168px;font-family:"Poppins",sans-serif;font-weight:700;font-size:34px;line-height:38px;color:var(--ink)}
  .hex{position:absolute;width:248px;text-align:center;color:var(--white)}
  .hex h3{font-size:15px;font-weight:700;margin:6px 0 8px}
  .hex p{font-size:11px;line-height:16px;padding:0 26px}
  .hex svg{display:block;margin:0 auto}

  /* Chart slide */
  .chart-slide{top:2565px}
  .chart-slide .media{left:0;top:0;right:0;height:253px;background:linear-gradient(180deg,#1b1b1b 0%,#2e2e2e 60%,#3b3b3b 100%)}
  .chart-heading{position:absolute;left:0;right:0;top:72px;text-align:center;font-family:"Poppins",sans-serif;font-weight:700;font-size:32px;color:var(--white)}
  .chart-card{position:absolute;left:82px;top:174px;width:875px;height:352px;background:var(--white);border-radius:4px;box-shadow:0 2px 10px rgba(0,0,0,.12)}
  .chart-card h4{position:absolute;left:28px;top:22px;font-size:14px;font-weight:700;color:#222}
  .legend{position:absolute;left:28px;top:52px;display:flex;gap:24px;font-size:10px;font-weight:500;color:#444}
  .legend span{display:flex;align-items:center;gap:7px}
  .legend i{width:8px;height:8px;border-radius:50%;display:inline-block}
  .select{position:absolute;left:648px;top:20px;width:180px;height:30px;border:1px solid var(--line);border-radius:3px;font-size:11px;font-weight:500;padding:8px 12px;color:#333}
  .select svg{position:absolute;right:10px;top:9px}
  .chart-svg{position:absolute;left:0;top:0}

  /* Closing slide */
  .closing{top:3195px}
  .disclaimer-title{position:absolute;left:69px;top:58px;font-family:"Poppins",sans-serif;font-weight:700;font-size:32px;color:var(--ink)}
  .disclaimer-text{position:absolute;left:69px;top:108px;width:918px;font-size:8.8px;letter-spacing:-0.1px;line-height:18px;color:#222}
  .contact{position:absolute;left:0;top:325px;width:507px;height:260px;background:var(--green);padding:56px 0 0 58px}
  .contact li{list-style:none;display:flex;align-items:center;gap:15px;height:38.5px;font-size:16px;font-weight:700;color:var(--white)}
  .contact svg{width:18px;height:18px;flex:none}
  .closing .media{left:507px;top:325px;right:0;bottom:0;background:linear-gradient(135deg,#f2f1f2 0%,#d8cfc8 40%,#6b4a3c 65%,#dedbe0 100%)}
</style>
</head>
<body>

<section class="slide cover">
  <div class="media" role="img" aria-label="City skyline blended with stacked coins and rising growth chart lines"></div>
  <div class="brand">
    <div class="brand-mark"></div>
    <div class="brand-name">VERANTA</div>
  </div>
  <p class="cover-tagline">Independent financial advisory<br>services tailored to your goals</p>
  <p class="cover-date">ABC, XYZ – <span>April 2021</span></p>
</section>

<section class="slide split intro">
  <div class="copy">
    <h2 class="slide-title">Introduction</h2>
    <p class="slide-sub">Nemo enim ipsam voluptatem<br>quia voluptas sit</p>
    <p class="lead">Sed ut perspiciatis unde omnis iste natus error sit voluptatem accusantium doloremque laudantium, totam rem aperiam, eaque ipsa quae ab illo inventore veritatis et quasi architecto beatae vitae dicta sunt explicabo. Nemo enim ipsam voluptatem quia voluptas sit aspernatur aut odit aut fugit, sed quia consequuntur magni dolores eos qui ratione voluptatem</p>
    <ul class="ticks">
      <li><svg viewBox="0 0 16 16"><circle cx="8" cy="8" r="8" fill="#7dbb2e"/><path d="M4 8h7M8 5l3 3-3 3" stroke="#fff" stroke-width="1.8" fill="none"/></svg>Nemo enim ipsam voluptatem quia voluptas<br>sit aspernatur aut odit aut fugit,</li>
      <li><svg viewBox="0 0 16 16"><circle cx="8" cy="8" r="8" fill="#7dbb2e"/><path d="M4 8h7M8 5l3 3-3 3" stroke="#fff" stroke-width="1.8" fill="none"/></svg>Nemo enim ipsam voluptatem quia voluptas<br>sit aspernatur aut odit aut fugit,</li>
      <li><svg viewBox="0 0 16 16"><circle cx="8" cy="8" r="8" fill="#7dbb2e"/><path d="M4 8h7M8 5l3 3-3 3" stroke="#fff" stroke-width="1.8" fill="none"/></svg>Nemo enim ipsam voluptatem quia voluptas<br>sit aspernatur aut odit aut fugit,</li>
      <li><svg viewBox="0 0 16 16"><circle cx="8" cy="8" r="8" fill="#7dbb2e"/><path d="M4 8h7M8 5l3 3-3 3" stroke="#fff" stroke-width="1.8" fill="none"/></svg>Nemo enim ipsam voluptatem quia voluptas<br>sit aspernatur aut odit aut fugit,</li>
    </ul>
  </div>
  <div class="media" role="img" aria-label="Potted tree whose leafy crown grows into an upward arrow against a concrete wall"></div>
</section>

<section class="slide services">
  <div class="media" role="img" aria-label="Dark toned photo of a business handshake"></div>
  <svg class="hex-grid" width="1040" height="585" viewBox="0 0 1040 585">
    <g fill="#7dbb2e" stroke="#fff" stroke-width="3">
      <polygon points="390,65 514,133 514,269 390,337 266,269 266,133"/>
      <polygon points="648,65 772,133 772,269 648,337 524,269 524,133"/>
      <polygon points="261,269 385,337 385,473 261,541 137,473 137,337"/>
      <polygon points="519,269 643,337 643,473 519,541 395,473 395,337"/>
      <polygon points="777,269 901,337 901,473 777,541 653,473 653,337"/>
    </g>
  </svg>
  <div class="hex" style="left:266px;top:108px">
    <svg width="52" height="46" viewBox="0 0 52 46" fill="none" stroke="#fff" stroke-width="1.6"><rect x="14" y="4" width="24" height="40"/><rect x="6" y="22" width="8" height="22"/><rect x="38" y="22" width="8" height="22"/><path d="M19 10h4M29 10h4M19 17h4M29 17h4M19 24h4M29 24h4M22 44v-10h8v10"/></svg>
    <h3>Family office</h3>
    <p>Sed ut perspiciatis unde omnis iste natus voluptatem accsantium launtium, totam rem aperiam, eaque ipsa quae ab illo inventore veritatis et quasi</p>
  </div>
  <div class="hex" style="left:524px;top:108px">
    <svg width="52" height="46" viewBox="0 0 52 46" fill="none" stroke="#fff" stroke-width="1.6"><path d="M4 44h44"/><rect x="8" y="30" width="6" height="14"/><rect x="18" y="24" width="6" height="20"/><rect x="28" y="16" width="6" height="28"/><rect x="38" y="8" width="6" height="36"/><path d="M6 24l12-8 8 4 16-16M36 4h6v6"/></svg>
    <h3>Alternative investments</h3>
    <p>Sed ut perspiciatis unde omnis iste natus voluptatem accsantium launtium, totam rem aperiam, eaque ipsa quae ab illo inventore veritatis et quasi</p>
  </div>
  <div class="hex" style="left:137px;top:312px">
    <svg width="52" height="46" viewBox="0 0 52 46" fill="none" stroke="#fff" stroke-width="1.6"><rect x="8" y="8" width="36" height="30" rx="2"/><path d="M4 42h44M14 30v-6M20 30v-10M26 30v-4M32 30v-12M38 30v-8"/><circle cx="26" cy="8" r="5"/></svg>
    <h3>Investment management</h3>
    <p>Sed ut perspiciatis unde omnis iste natus voluptatem accsantium launtium, totam rem aperiam, eaque ipsa quae ab illo inventore veritatis et quasi</p>
  </div>
  <div class="hex" style="left:395px;top:312px">
    <svg width="52" height="46" viewBox="0 0 52 46" fill="#fff"><rect x="6" y="20" width="8" height="24"/><rect x="18" y="28" width="8" height="16"/><rect x="30" y="32" width="8" height="12"/><path d="M6 6l14 12 10 4 14 14-2 2-13-12-10-4L4 8z"/><path d="M4 44h44v1H4z"/></svg>
    <h3>Financial planning</h3>
    <p>Sed ut perspiciatis unde omnis iste natus voluptatem accsantium launtium, totam rem aperiam, eaque ipsa quae ab illo inventore veritatis et quasi</p>
  </div>
  <div class="hex" style="left:653px;top:312px">
    <svg width="52" height="46" viewBox="0 0 52 46" fill="none" stroke="#fff" stroke-width="1.6"><rect x="16" y="4" width="20" height="14" rx="2"/><circle cx="10" cy="22" r="4"/><circle cx="42" cy="22" r="4"/><path d="M2 40v-6a8 8 0 0 1 16 0v6M34 40v-6a8 8 0 0 1 16 0v6M18 32h16M26 18v14"/></svg>
    <h3>Consulting</h3>
    <p>Sed ut perspiciatis unde omnis iste natus voluptatem accsantium launtium, totam rem aperiam, eaque ipsa quae ab illo inventore veritatis et quasi</p>
  </div>
  <h2 class="services-title">Our<br>Services</h2>
</section>

<section class="slide split meeting">
  <div class="copy">
    <h2 class="slide-title">Sed ut perspiciatis</h2>
    <p class="slide-sub">Nemo enim ipsam voluptatem<br>quia voluptas sit</p>
    <p class="lead">Sed ut perspiciatis unde omnis iste natus error sit voluptatem accusantium doloremque laudantium, totam rem aperiam, eaque ipsa quae ab illo inventore veritatis et quasi architecto beatae vitae dicta sunt explicabo. Nemo enim ipsam voluptatem quia voluptas sit aspernatur aut odit aut fugit, sed quia consequuntur magni dolores eos qui ratione voluptatem</p>
    <ul class="ticks">
      <li><svg viewBox="0 0 16 16"><circle cx="8" cy="8" r="8" fill="#7dbb2e"/><path d="M4 8h7M8 5l3 3-3 3" stroke="#fff" stroke-width="1.8" fill="none"/></svg>Nemo enim ipsam voluptatem quia voluptas<br>sit aspernatur aut odit aut fugit,</li>
      <li><svg viewBox="0 0 16 16"><circle cx="8" cy="8" r="8" fill="#7dbb2e"/><path d="M4 8h7M8 5l3 3-3 3" stroke="#fff" stroke-width="1.8" fill="none"/></svg>Nemo enim ipsam voluptatem quia voluptas<br>sit aspernatur aut odit aut fugit,</li>
      <li><svg viewBox="0 0 16 16"><circle cx="8" cy="8" r="8" fill="#7dbb2e"/><path d="M4 8h7M8 5l3 3-3 3" stroke="#fff" stroke-width="1.8" fill="none"/></svg>Nemo enim ipsam voluptatem quia voluptas<br>sit aspernatur aut odit aut fugit,</li>
      <li><svg viewBox="0 0 16 16"><circle cx="8" cy="8" r="8" fill="#7dbb2e"/><path d="M4 8h7M8 5l3 3-3 3" stroke="#fff" stroke-width="1.8" fill="none"/></svg>Nemo enim ipsam voluptatem quia voluptas<br>sit aspernatur aut odit aut fugit,</li>
    </ul>
  </div>
  <div class="media" role="img" aria-label="Team around a wooden table reviewing printed financial charts with a coffee mug"></div>
</section>

<section class="slide chart-slide">
  <div class="media" role="img" aria-label="Dark city skyline with rising arrows"></div>
  <h2 class="chart-heading">Nemo enim ipsam voluptatem quia</h2>
  <div class="chart-card">
    <h4>Nemo enim ipsam voluptatem quia</h4>
    <div class="legend"><span><i style="background:var(--bar-grey)"></i>Label 1</span><span><i style="background:var(--green)"></i>Label 2</span></div>
    <div class="select">Year<svg width="8" height="12" viewBox="0 0 8 12" fill="#888"><path d="M4 0l4 5H0zM4 12L0 7h8z"/></svg></div>
    <svg class="chart-svg" width="875" height="352" viewBox="0 0 875 352" font-family="Montserrat, sans-serif" font-size="9" fill="#444">
      <g text-anchor="end">
        <text x="56" y="110">20K</text><text x="56" y="157">15K</text><text x="56" y="204">10K</text><text x="56" y="251">5K</text><text x="56" y="297">0</text>
      </g>
      <g fill="#c9c9c9">
        <rect x="77" y="135" width="43" height="159"/><rect x="142" y="154" width="43" height="140"/><rect x="207" y="121" width="43" height="173"/><rect x="272" y="157" width="43" height="137"/><rect x="337" y="124" width="43" height="170"/><rect x="402" y="112" width="43" height="182"/><rect x="467" y="182" width="43" height="112"/><rect x="532" y="135" width="43" height="159"/><rect x="597" y="119" width="43" height="175"/><rect x="662" y="124" width="43" height="170"/><rect x="727" y="157" width="43" height="137"/><rect x="792" y="124" width="43" height="170"/>
      </g>
      <g fill="#7dbb2e">
        <rect x="77" y="226" width="43" height="68"/><rect x="142" y="191" width="43" height="103"/><rect x="207" y="182" width="43" height="112"/><rect x="272" y="199" width="43" height="95"/><rect x="337" y="215" width="43" height="79"/><rect x="402" y="172" width="43" height="122"/><rect x="467" y="245" width="43" height="49"/><rect x="532" y="161" width="43" height="133"/><rect x="597" y="182" width="43" height="112"/><rect x="662" y="200" width="43" height="94"/><rect x="727" y="191" width="43" height="103"/><rect x="792" y="163" width="43" height="131"/>
      </g>
      <g>
        <rect x="531" y="94" width="45" height="30" rx="3" fill="#fff" stroke="#ddd"/>
        <text x="553" y="104" text-anchor="middle" font-size="6" fill="#888">AUG</text>
        <text x="553" y="118" text-anchor="middle" font-size="12" font-weight="700" fill="#222">14.2K</text>
      </g>
      <g text-anchor="middle">
        <text x="98" y="320">Jan</text><text x="163" y="320">Feb</text><text x="228" y="320">Mar</text><text x="293" y="320">Apr</text><text x="358" y="320">May</text><text x="423" y="320">Jun</text><text x="488" y="320">Jul</text><text x="553" y="320">Aug</text><text x="618" y="320">Sep</text><text x="683" y="320">Oct</text><text x="748" y="320">Nov</text><text x="813" y="320">Dec</text>
      </g>
    </svg>
  </div>
</section>

<section class="slide closing">
  <h2 class="disclaimer-title">Disclaimer</h2>
  <p class="disclaimer-text">Disclaimer: this document is a general communication being provided for informational purposes only. It is educational in nature and not designed to be taken as advice or a recommendation for any specific investment product, strategy, plan feature or other purpose in any jurisdiction. Any examples used are generic, hypothetical and for illustration purposes only. This material does not contain sufficient information to support an investment decision and it should not be relied upon by you in evaluating the merits of investing in any securities or products. In addition, users should make an independent assessment of the legal, regulatory, tax, credit, and accounting implications and determine, together with their own professional advisers, if any investment mentioned herein is believed to be suitable to their personal goals. Investors should ensure that they obtain all available relevant information before making any investment. Any forecasts, figures, opinions or investment techniques and strategies set out are for information purposes only, based on certain assumptions and current market conditions and are subject to change without prior notice. All information presented herein is considered to be accurate at the time of production, but no warranty of accuracy is given and no liability in respect of any error or omission is accepted. It should be noted that investment involves risks, the value of investments and the income from them may fluctuate in accordance with market conditions and taxation agreements and investors may not get back the full amount invested. Both past performance and yields are not reliable indicators of current and future results.</p>
  <ul class="contact">
    <li><svg viewBox="0 0 24 24" fill="#fff"><path d="M6.6 10.8a15.1 15.1 0 0 0 6.6 6.6l2.2-2.2a1 1 0 0 1 1-.25 11.4 11.4 0 0 0 3.6.57 1 1 0 0 1 1 1V20a1 1 0 0 1-1 1A17 17 0 0 1 3 4a1 1 0 0 1 1-1h3.5a1 1 0 0 1 1 1c0 1.25.2 2.45.57 3.570a1 1 0 0 1-.25 1z"/></svg>+1 412 555 0187</li>
    <li><svg viewBox="0 0 24 24" fill="none" stroke="#fff" stroke-width="2"><circle cx="12" cy="12" r="9"/><path d="M3 12h18M12 3c3 3 3 15 0 18M12 3c-3 3-3 15 0 18"/></svg>www.veranta-advisors.com</li>
    <li><svg viewBox="0 0 24 24" fill="#fff"><path d="M2 5h20v14H2z"/><path d="M2 5l10 8 10-8" stroke="#7dbb2e" stroke-width="2" fill="none"/></svg>hello@veranta-advisors.com</li>
    <li><svg viewBox="0 0 24 24" fill="#fff"><path d="M12 2a7 7 0 0 0-7 7c0 5 7 13 7 13s7-8 7-13a7 7 0 0 0-7-7zm0 9.5A2.5 2.5 0 1 1 12 6.5a2.5 2.5 0 0 1 0 5z"/></svg>4345 Larkfield Avenue, Pittsburgh PA 15224</li>
  </ul>
  <div class="media" role="img" aria-label="Two smiling colleagues working together at a desk"></div>
</section>

</body>
</html>
```